bright frame masters

we are a window and door installation company for residential and commercial buildings

These cards are for Colin Mercer
His email is colin@brightframemastersco.com and he is a project manager.

Are colors are white red and black

I want all of his information on the card and a few pictures of windows and doors

```html
<!DOCTYPE html>
<html lang="en">
<head>
<meta charset="utf-8">
<title>Bright Frame Masters – Business Card</title>
<link href="https://fonts.googleapis.com/css2?family=Tinos:wght@400;700&display=swap" rel="stylesheet">
<style>
  :root {
    --brand-red: #a81a37;
    --ink: #1c1c1c;
    --ink-soft: #444444;
    --paper: #ffffff;
    --stage: #9a9a9a;
  }
  * { margin: 0; padding: 0; box-sizing: border-box; }
  html, body { width: 1200px; height: 1059px; overflow: hidden; }
  body {
    position: relative;
    background: var(--stage);
    font-family: "Tinos", "Times New Roman", serif;
    color: var(--ink);
  }
  .card {
    position: absolute;
    width: 720px;
    height: 409px;
    border-radius: 24px;
    overflow: hidden;
  }
  .card-front { left: 259px; top: 79px; background: var(--paper); box-shadow: 0 10px 18px rgba(0,0,0,.35); }
  .card-back { left: 245px; top: 570px; background: var(--brand-red); box-shadow: 0 10px 18px rgba(0,0,0,.35); }

  .accent-bar { position: absolute; left: 2px; top: 53px; width: 9px; height: 42px; background: var(--brand-red); }
  .person-name { position: absolute; left: 30px; top: 46px; font-size: 28px; font-weight: 700; color: var(--brand-red); line-height: 1; }
  .person-title { position: absolute; left: 30px; top: 84px; font-size: 19px; line-height: 1; }

  .contact-list { position: absolute; left: 28px; top: 150px; list-style: none; }
  .contact-item { display: flex; align-items: center; height: 33px; font-size: 18px; }
  .contact-item svg { width: 20px; height: 20px; margin-right: 11px; fill: var(--brand-red); flex: none; }
  .address { position: absolute; left: 28px; top: 251px; font-size: 18px; line-height: 26px; color: var(--ink-soft); }

  .band { position: absolute; left: 0; top: 0; width: 720px; height: 409px; }
  .band-text { position: absolute; left: 27px; top: 340px; font-size: 24px; font-weight: 700; color: var(--paper); line-height: 29px; }

  .brand-name { position: absolute; left: 419px; top: 112px; font-size: 43px; font-weight: 700; color: var(--brand-red); line-height: 54px; letter-spacing: 0.5px; }
  .brand-phone { position: absolute; left: 419px; top: 298px; font-size: 44px; font-weight: 700; color: var(--brand-red); line-height: 1; }

  .photo { position: absolute; }
  .photo-townhouse { left: 30px; top: 31px; width: 215px; height: 143px; background: linear-gradient(180deg, #b8c4d4, #8e9aa8 70%, #4a4a4a); }
  .photo-atrium { left: 252px; top: 32px; width: 212px; height: 140px; background: linear-gradient(135deg, #3a3a36, #8a9a6a 55%, #d9d6cc); }
  .photo-frames { left: 473px; top: 35px; width: 229px; height: 139px; background: linear-gradient(90deg, #d9a25a, #f0e4cc 45%, #b0713e 75%, #f2c27a); }
  .photo-forest-window { left: 28px; top: 183px; width: 202px; height: 200px; background: linear-gradient(180deg, #e6dfe8, #5c9a3a 45%, #2f6a24); }
  .photo-sliding-door { left: 243px; top: 188px; width: 220px; height: 201px; background: linear-gradient(180deg, #ece0dc, #d8cfca 60%, #c9b9a4); }
  .photo-french-doors { left: 480px; top: 189px; width: 220px; height: 200px; background: linear-gradient(180deg, #f2f4f5, #7e4a32 50%, #e8eef0); }
</style>
</head>
<body>
  <section class="card card-front">
    <svg class="band" viewBox="0 0 720 409" aria-hidden="true">
      <polygon points="0,334 342,334 393,378 720,378 720,409 0,409" fill="var(--brand-red)"/>
    </svg>
    <div class="accent-bar"></div>
    <h1 class="person-name">Colin Mercer</h1>
    <p class="person-title">Project Manager</p>
    <ul class="contact-list">
      <li class="contact-item">
        <svg viewBox="0 0 24 24" aria-hidden="true"><path d="M6.6 10.8a15.1 15.1 0 0 0 6.6 6.6l2.2-2.2c.3-.3.7-.4 1-.2 1.1.4 2.3.6 3.6.6.6 0 1 .4 1 1V20c0 .6-.4 1-1 1C10.6 21 3 13.4 3 4c0-.6.4-1 1-1h3.5c.6 0 1 .4 1 1 0 1.3.2 2.5.6 3.6.1.3 0 .7-.2 1z"/></svg>
        (555) 014-2286
      </li>
      <li class="contact-item">
        <svg viewBox="0 0 24 24" aria-hidden="true"><path d="M2 5h20v14H2z M2 5l10 7 10-7" fill="var(--brand-red)"/><path d="M3 6l9 6.3L21 6" fill="none" stroke="#fff" stroke-width="1.6"/></svg>
        colin@brightframemastersco.com
      </li>
      <li class="contact-item">
        <svg viewBox="0 0 24 24" aria-hidden="true"><circle cx="12" cy="12" r="10"/><path d="M2 12h20M12 2c3 3 3 17 0 20M12 2c-3 3-3 17 0 20" fill="none" stroke="#fff" stroke-width="1.4"/></svg>
        www.websitename.com
      </li>
    </ul>
    <p class="address">421, Address line goes here<br>45452, Country name</p>
    <p class="band-text">Window and Door Company<br>Commercial and Residential</p>
    <p class="brand-name">BRIGHT<br>FRAME<br>MASTERS</p>
    <p class="brand-phone">(555) 014-2286</p>
  </section>

  <section class="card card-back">
    <div class="photo photo-townhouse" role="img" aria-label="Photo of a pale blue townhouse front with a black door and white sash windows"></div>
    <div class="photo photo-atrium" role="img" aria-label="Photo of a modern interior with a tall black-framed glass wall and doors"></div>
    <div class="photo photo-frames" role="img" aria-label="Photo of several window frames in white, wood and aluminium finishes"></div>
    <div class="photo photo-forest-window" role="img" aria-label="Photo of open white casement windows looking onto a green forest path"></div>
    <div class="photo photo-sliding-door" role="img" aria-label="Photo of white sliding glass doors in an empty room"></div>
    <div class="photo photo-french-doors" role="img" aria-label="Photo of three wooden glass-panel doors in a white room"></div>
  </section>
</body>
</html>
```